PSD website for property company

Please read the brief thoroughly.

We are looking for a new website for a property group that does property acquisitions, property development and property management.
They buy, build and lease core inner city industrial assets in Sydney, Australia.
They also invest in residential developments.

Site menu
- Home page
- Property – sub menus include – Leasing ; Projects ; Investments ; Property Management
- Capital and finance
- About
- Contact

They like this website
https://www.verlo.com.au/

They want the site to be clean, modern and bold.
They like few colors, even black and white is OK to submit

They have a logo and style guide and useable images here:
http://www.kumet.net/temp/PelorisWeb2019.zip
The zip file is also attached to this project.
We have supplied some images to give you an idea, but we will also require you to provide at least 3 extra images from stock photos.
Use your imagination.

I am expecting a lot of similar designs, so be aware the photos you choose will be really important.
They want really 3 good stock photos used and supplied without charge.
Please not too generic, I repeat the quality of the photos is important.
You may provide several photos (but not in multiple submissions please) and we will choose the best three to be provided.

The winner will be selected on a single home page design and required to provide;
All photos use in original format without charge
A second ‘standard page’ template design based on the winning home page design

```html
<!DOCTYPE html>
<html lang="en">
<head>
<meta charset="utf-8">
<title>Peloris — Property Group</title>
<link rel="stylesheet" href="https://fonts.googleapis.com/css2?family=Montserrat:wght@400;500;600;700&family=Lato:wght@400;700;900&display=swap">
<style>
:root{
  --orange:#f9a602;
  --green:#8dc63f;
  --ink:#1f1f1f;
  --text:#555;
  --muted:#777;
  --white:#fff;
  --band:#2c2c2c;
  --footer:#222;
}
*{margin:0;padding:0;box-sizing:border-box}
html,body{width:1200px;height:3698px;overflow:hidden;background:var(--white)}
body{position:relative;font-family:'Lato',sans-serif;color:var(--text)}
.abs{position:absolute}
h1,h2,h3,h4{font-family:'Montserrat',sans-serif;font-weight:500;color:var(--ink)}
.btn{position:absolute;background:var(--orange);color:var(--white);font-family:'Lato',sans-serif;font-weight:900;font-size:16px;text-transform:uppercase;display:flex;align-items:center;justify-content:center;letter-spacing:.3px}

/* header */
.site-header{position:absolute;left:0;top:0;width:1200px;height:95px;background:var(--white);z-index:5}
.nav-item{position:absolute;top:35px;font-family:'Montserrat',sans-serif;font-size:16px;font-weight:500;color:var(--ink)}
.nav-item.active{color:var(--orange)}
.logo-disc{position:absolute;left:517px;top:-20px;width:166px;height:166px;border-radius:50%;background:var(--white);z-index:6;display:flex;align-items:center;justify-content:center}
.logo-name{font-family:'Montserrat',sans-serif;font-weight:500;font-size:30px;color:var(--ink);margin-top:20px}
.header-icon{position:absolute;top:36px}

/* hero */
.hero{position:absolute;left:0;top:95px;width:1200px;height:555px;background:linear-gradient(90deg,#8d939a 0%,#a8adb0 30%,#6b5448 55%,#4e3b31 75%,#9aa3a6 100%)}
.hero-shade{position:absolute;inset:0;background:linear-gradient(180deg,rgba(0,0,0,0) 60%,rgba(40,45,35,.55) 100%)}
.hero-title{position:absolute;left:84px;top:143px;font-family:'Montserrat',sans-serif;font-weight:700;font-size:84px;color:var(--white);letter-spacing:1px}
.hero-text{position:absolute;left:87px;top:245px;width:560px;font-size:20px;line-height:32px;color:var(--white)}
.slide-arrow{position:absolute;top:257px;width:42px;height:42px;border-radius:50%;background:rgba(255,255,255,.35);display:flex;align-items:center;justify-content:center}

/* services */
.section-title{position:absolute;left:0;width:1200px;text-align:center;font-size:46px}
.service{position:absolute;width:405px;height:396px}
.service svg.shape{position:absolute;inset:0}
.service-icon{position:absolute;left:162px;top:72px}
.service-name{position:absolute;left:0;top:180px;width:405px;text-align:center;font-family:'Montserrat',sans-serif;font-size:22px;font-weight:500;color:var(--white)}
.service-text{position:absolute;left:90px;top:220px;width:225px;text-align:center;font-size:16px;line-height:30px;color:var(--white)}
.service-more{position:absolute;left:195px;top:333px}

/* capital */
.capital{position:absolute;left:0;top:1305px;width:1200px;height:685px}
.capital-title{position:absolute;left:90px;top:172px;font-size:47px;color:var(--white)}
.capital-text{position:absolute;left:91px;top:245px;width:590px;font-size:16px;line-height:36px;color:var(--white);text-align:justify}

/* featured */
.card{position:absolute;top:2153px;width:320px;height:430px;background:var(--white);box-shadow:0 2px 10px rgba(0,0,0,.14)}
.card-media{position:absolute;left:8px;top:9px;width:304px;height:202px}
.card-tools{position:absolute;left:15px;top:15px;display:flex;gap:6px}
.card-tool{width:28px;height:28px;background:rgba(40,40,40,.75);display:flex;align-items:center;justify-content:center}
.card-title{position:absolute;left:0;top:238px;width:320px;text-align:center;font-size:23px}
.card-text{position:absolute;left:38px;top:276px;width:244px;text-align:center;font-size:15px;line-height:28px;color:var(--muted)}
.card .btn{left:97px;top:369px;width:126px;height:35px;font-size:14px}

/* about */
.about-title{position:absolute;left:555px;top:2740px;font-size:48px}
.about-text{position:absolute;left:556px;top:2808px;width:553px;font-size:16px;line-height:36px;text-align:justify}

/* contact band & footer */
.contact-band{position:absolute;left:0;top:3199px;width:1200px;height:120px;background:var(--band)}
.contact-item{position:absolute;top:30px;display:flex;align-items:center;gap:14px;color:var(--white);font-size:16px;line-height:22px}
.pin{width:46px;height:46px;border-radius:50%;background:var(--orange);display:flex;align-items:center;justify-content:center;flex:none}
.site-footer{position:absolute;left:0;top:3319px;width:1200px;height:379px;background:var(--footer);color:var(--white)}
.footer-brand{position:absolute;left:95px;top:90px;font-family:'Montserrat',sans-serif;font-weight:500;font-size:30px;color:var(--white)}
.footer-col{position:absolute;top:52px}
.footer-col h4{color:var(--white);font-size:18px;font-weight:500;margin-bottom:18px}
.footer-col li{list-style:none;font-size:13px;line-height:27px;color:var(--white)}
.newsletter-text{font-size:14px;margin-bottom:14px}
.newsletter-field{width:322px;height:45px;border:1px solid #ddd;display:flex;align-items:center;justify-content:space-between;padding:0 14px;font-size:12px}
.socials{position:absolute;left:505px;top:256px;display:flex;gap:9px}
.social{width:41px;height:41px;border-radius:50%;background:var(--orange)}
.footer-rule{position:absolute;left:80px;top:326px;width:1040px;height:1px;background:#333}
.copyright{position:absolute;left:0;top:340px;width:1200px;text-align:center;font-size:12px}
</style>
</head>
<body>

<header class="site-header">
  <span class="nav-item active" style="left:85px">Home</span>
  <span class="nav-item" style="left:172px">Property ▾</span>
  <span class="nav-item" style="left:288px">Capital and finance</span>
  <span class="nav-item" style="left:773px">About</span>
  <span class="nav-item" style="left:861px">Contact</span>
  <svg class="header-icon" style="left:984px" width="16" height="16" viewBox="0 0 16 16"><circle cx="6.5" cy="6.5" r="5" fill="none" stroke="#1f1f1f" stroke-width="2"/><line x1="10" y1="10" x2="15" y2="15" stroke="#1f1f1f" stroke-width="2.5"/></svg>
  <svg class="header-icon" style="left:1036px;top:38px" width="17" height="13" viewBox="0 0 17 13"><rect width="17" height="13" rx="1" fill="#1f1f1f"/><path d="M1 1l7.5 6L16 1" fill="none" stroke="#fff" stroke-width="1.5"/></svg>
  <svg class="header-icon" style="left:1093px" width="14" height="15" viewBox="0 0 14 15"><circle cx="7" cy="4" r="4" fill="#1f1f1f"/><path d="M0 15c0-5 3-7 7-7s7 2 7 7z" fill="#1f1f1f"/></svg>
</header>
<div class="logo-disc"><span class="logo-name">Peloris</span></div>

<section class="hero" role="img" aria-label="Photo of a modern brick apartment building with arched ground-floor shopfronts and street trees">
  <div class="hero-shade"></div>
  <h1 class="hero-title">PELORIS</h1>
  <p class="hero-text">Lorem ipsum dolor sit amet, consectetur adipiscing elit, abore et dolore magna aliqua. Ut enim adris</p>
  <span class="btn" style="left:89px;top:346px;width:182px;height:50px">Get Started</span>
  <div class="slide-arrow" style="left:24px"><svg width="12" height="16"><path d="M9 2L3 8l6 6" fill="none" stroke="#fff" stroke-width="2"/></svg></div>
  <div class="slide-arrow" style="left:1135px"><svg width="12" height="16"><path d="M3 2l6 6-6 6" fill="none" stroke="#fff" stroke-width="2"/></svg></div>
</section>

<h2 class="section-title" style="top:740px">What We Do</h2>

<div class="service" style="left:66px;top:814px">
  <svg class="shape" viewBox="0 0 405 396"><polygon points="202.5,0 405,198 202.5,396 0,198" fill="#f9a602"/></svg>
  <svg class="service-icon" width="82" height="82" viewBox="0 0 82 82" fill="none" stroke="#fff" stroke-width="3"><circle cx="41" cy="44" r="24"/><path d="M41 6v10M41 72v10M3 44h10M69 44h10"/><path d="M28 46l13-12 13 12M32 43v12h18V43"/></svg>
  <div class="service-name">Property Development</div>
  <p class="service-text">Lorem ipsum dolor sit amet, consectetur adipiscing elit, sed tempor incididunt</p>
  <svg class="service-more" width="14" height="12"><path d="M2 1l5 4 5-4M2 6l5 4 5-4" fill="none" stroke="#fff" stroke-width="1.5"/></svg>
</div>
<div class="service" style="left:397px;top:814px">
  <svg class="shape" viewBox="0 0 405 396"><polygon points="202.5,0 405,198 202.5,396 0,198" fill="#8dc63f"/></svg>
  <svg class="service-icon" width="82" height="82" viewBox="0 0 82 82" fill="none" stroke="#fff" stroke-width="3"><path d="M20 22l21-12 21 12zM24 26v20M34 26v20M48 26v20M58 26v20M20 48h42"/><path d="M4 50l12 24h10M78 50l-12 24H56"/></svg>
  <div class="service-name">Property Acquisitions</div>
  <p class="service-text">Lorem ipsum dolor sit amet, consectetur adipiscing elit, sed tempor incididunt</p>
  <svg class="service-more" width="14" height="12"><path d="M2 1l5 4 5-4M2 6l5 4 5-4" fill="none" stroke="#fff" stroke-width="1.5"/></svg>
</div>
<div class="service" style="left:728px;top:814px">
  <svg class="shape" viewBox="0 0 405 396"><polygon points="202.5,0 405,198 202.5,396 0,198" fill="#f9a602"/></svg>
  <svg class="service-icon" width="82" height="82" viewBox="0 0 82 82" fill="none" stroke="#fff" stroke-width="3"><rect x="44" y="10" width="30" height="50"/><path d="M52 20h4M62 20h4M52 30h4M62 30h4M52 40h4M62 40h4"/><circle cx="28" cy="36" r="12"/><path d="M6 76c0-12 10-18 22-18s22 6 22 18"/></svg>
  <div class="service-name">Property Management</div>
  <p class="service-text">Lorem ipsum dolor sit amet, consectetur adipiscing elit, sed tempor incididunt</p>
  <svg class="service-more" width="14" height="12"><path d="M2 1l5 4 5-4M2 6l5 4 5-4" fill="none" stroke="#fff" stroke-width="1.5"/></svg>
</div>

<section class="capital">
  <svg class="abs" style="left:0;top:0" width="1200" height="685" viewBox="0 0 1200 685">
    <defs>
      <linearGradient id="capitalPhoto" x1="0" y1="0" x2="1" y2="1">
        <stop offset="0" stop-color="#4a4a48"/><stop offset=".5" stop-color="#5b4a40"/><stop offset="1" stop-color="#3a3029"/>
      </linearGradient>
    </defs>
    <polygon points="426,74 600,4 774,74" fill="#f9a602"/>
    <polygon points="426,678 600,677 774,678 600,677" fill="#f9a602"/>
    <polygon points="426,605 774,605 600,677" fill="#f9a602"/>
    <polygon points="0,74 434,74 600,10 766,74 1200,74 1200,605 766,605 600,670 434,605 0,605" fill="url(#capitalPhoto)" role="img" aria-label="Photo of brick townhouses with large arched windows along a busy street"/>
  </svg>
  <h2 class="capital-title">Capital and finance</h2>
  <p class="capital-text">Lorem ipsum dolor sit amet, consectetur adipiscing elit, sed do eiusmod tempor incididunt ut labore et dolore magna aliqua. Ut enim ad minim veniam, quis nostrud exercitation ullamco laboris nisi ut aliquip ex ea commodo consequat. Duis aute irure dolor in reprehenderit in voluptate velit esse cillum dolore eu fugiat nulla iatur. Excepteur sint occaecat cupidatat non proident.</p>
  <span class="btn" style="left:92px;top:449px;width:170px;height:50px">Read More</span>
</section>

<h2 class="section-title" style="top:2072px">Featured Properties</h2>

<article class="card" style="left:82px">
  <div class="card-media" role="img" aria-label="Photo of a suburban street of new brick townhouses" style="background:linear-gradient(180deg,#a9c6e0 0%,#c9d7df 40%,#8a6a52 65%,#9aa08a 100%)">
    <div class="card-tools"><span class="card-tool"><svg width="14" height="11"><rect y="2" width="14" height="9" rx="1" fill="#fff"/><circle cx="7" cy="6.5" r="2.5" fill="#333"/></svg></span><span class="card-tool"><svg width="12" height="12"><path d="M6 1v10M1 6h10" stroke="#fff" stroke-width="2.5"/></svg></span></div>
  </div>
  <h3 class="card-title">Lorem ipsum dolor</h3>
  <p class="card-text">Lorem ipsum dolor sit amet, consectetur adipiscing elit, sed do eiusmod tempor</p>
  <span class="btn">View More</span>
</article>
<article class="card" style="left:440px">
  <div class="card-media" role="img" aria-label="Photo looking up at glass city office towers" style="background:linear-gradient(135deg,#6f9fd6 0%,#2c3f7a 40%,#1a2440 60%,#b9c4cf 100%)">
    <div class="card-tools"><span class="card-tool"><svg width="14" height="11"><rect y="2" width="14" height="9" rx="1" fill="#fff"/><circle cx="7" cy="6.5" r="2.5" fill="#333"/></svg></span><span class="card-tool"><svg width="12" height="12"><path d="M6 1v10M1 6h10" stroke="#fff" stroke-width="2.5"/></svg></span></div>
  </div>
  <h3 class="card-title">Lorem ipsum dolor</h3>
  <p class="card-text">Lorem ipsum dolor sit amet, consectetur adipiscing elit, sed do eiusmod tempor</p>
  <span class="btn">View More</span>
</article>
<article class="card" style="left:797px">
  <div class="card-media" role="img" aria-label="Photo of a modern white coastal house with blue glass balconies" style="background:linear-gradient(180deg,#4e8fd0 0%,#a9cbe8 35%,#e8eef2 55%,#3d6f8f 75%,#5c7a4a 100%)">
    <div class="card-tools"><span class="card-tool"><svg width="14" height="11"><rect y="2" width="14" height="9" rx="1" fill="#fff"/><circle cx="7" cy="6.5" r="2.5" fill="#333"/></svg></span><span class="card-tool"><svg width="12" height="12"><path d="M6 1v10M1 6h10" stroke="#fff" stroke-width="2.5"/></svg></span></div>
  </div>
  <h3 class="card-title">Lorem ipsum dolor</h3>
  <p class="card-text">Lorem ipsum dolor sit amet, consectetur adipiscing elit, sed do eiusmod tempor</p>
  <span class="btn">View More</span>
</article>

<svg class="abs" style="left:88px;top:2693px" width="420" height="404" viewBox="0 0 420 404">
  <defs>
    <linearGradient id="aboutPhoto" x1="0" y1="0" x2="0" y2="1">
      <stop offset="0" stop-color="#9fb8cc"/><stop offset=".45" stop-color="#c8c6bf"/><stop offset=".7" stop-color="#6e6a5e"/><stop offset="1" stop-color="#7a8a5a"/>
    </linearGradient>
  </defs>
  <polygon points="200,5 406,200 200,395 0,200" fill="#fde6bd"/>
  <polygon points="207,4 410,205 207,402 4,205" fill="url(#aboutPhoto)" role="img" aria-label="Photo of a pale modern mixed-use building with arched colonnade and landscaping"/>
</svg>
<h2 class="about-title">About</h2>
<p class="about-text">Lorem ipsum dolor sit amet, consectetur adipiscing elit, sed do eiusmod tempor incididunt ut labore et dolore magna aliqua. Ut enim ad minim veniam, quis nostrud exercitation ullamco laboris nisi ut aliquip ex ea commodo quat. Duis aute irure dolor in reprehenderit in voluptate velit esse cillum dolore eu fugiat nulla iatur. Excepteur sint occaecat cupidatat non proident.</p>
<span class="btn" style="left:556px;top:3016px;width:171px;height:50px">Read More</span>

<section class="contact-band">
  <div class="contact-item" style="left:90px">
    <span class="pin"><svg width="16" height="22"><path d="M8 1a7 7 0 0 0-7 7c0 5 7 13 7 13s7-8 7-13a7 7 0 0 0-7-7z" fill="#fff"/><circle cx="8" cy="8" r="2.5" fill="#f9a602"/></svg></span>
    <span>Peloris,Unit 12,48 Harbour Lane Sydney<br>Australia</span>
  </div>
  <div class="contact-item" style="left:534px;top:32px">
    <span class="pin"><svg width="18" height="13"><rect width="18" height="13" rx="1" fill="#fff"/><path d="M1 1l8 6 8-6" fill="none" stroke="#f9a602" stroke-width="1.5"/></svg></span>
    <span>Email:<br>info@peloris-group.com</span>
  </div>
  <div class="contact-item" style="left:926px;top:36px">
    <span class="pin"><svg width="18" height="18" viewBox="0 0 18 18"><path d="M4 1l3 4-2 2c1 3 3 5 6 6l2-2 4 3-2 3C8 17 1 10 1 3z" fill="#fff"/></svg></span>
    <span>+61 2 9000 4812</span>
  </div>
</section>

<footer class="site-footer">
  <div class="footer-brand">Peloris</div>
  <div class="footer-col" style="left:314px">
    <h4>QUICK LINKS</h4>
    <ul><li>Home page</li><li>Property</li><li>Capital and<br>finance</li><li>About</li><li>Contact</li></ul>
  </div>
  <div class="footer-col" style="left:540px">
    <h4>OTHER LINKS</h4>
    <ul><li>Faq</li><li>Praivacy Policy</li><li>Terms &amp; Conditions</li></ul>
  </div>
  <div class="footer-col" style="left:787px">
    <h4>NEWSLETTER</h4>
    <p class="newsletter-text">Lorem ipsum dolor sit amet, consectetur</p>
    <div class="newsletter-field"><span>Enter Your Email Address</span><svg width="16" height="16" viewBox="0 0 16 16"><path d="M15 1L1 7l5 2 2 6z" fill="#fff"/></svg></div>
  </div>
  <div class="socials" aria-label="Social links">
    <span class="social"></span><span class="social"></span><span class="social"></span><span class="social"></span>
  </div>
  <div class="footer-rule"></div>
  <p class="copyright">© Copyrights.2019.The Company Name.All Rights Reserved</p>
</footer>

</body>
</html>
```